Halvern Partners M&A Email Newsletter Design

Halvern Partners is a Marketing/Consulting/M&A company and we want to find a graphic designer experienced in newsletter design. Please visit our website for more information and to see our logo. We would like the color scheme of the newsletter to reflect our colors of blue, yellow, and dark gray (see website for visual representation). The newsletter will focus on detailing M&A news in the market. Please reach out if you have any questions. https://www.halvernpartners.example/

Industry/Entity Type

Marketing

Font styles to use
Serif
Sans Serif

Colors
0456a4
ffc214
ffcf3e

Requirements
Must have
• Halvern Partners' Color Scheme: Yellow, Blue, Dark Gray (see website)
Professional economics newsletter
Should not have
• Strange/hard to read fonts

```html
<!DOCTYPE html>
<html lang="en">
<head>
<meta charset="utf-8">
<title>Halvern Partners — M&amp;A Transactions</title>
<link rel="stylesheet" href="https://fonts.googleapis.com/css2?family=Roboto:wght@300;400;500&family=Varela+Round&display=swap">
<style>
  :root {
    --blue: #0456a4;
    --yellow: #ffc214;
    --yellow-soft: #ffcf3e;
    --gold-text: #e6b40f;
    --ink: #2b2b2b;
    --gray: #555;
    --white: #fff;
  }
  * { box-sizing: border-box; margin: 0; padding: 0; }
  html, body { width: 1200px; height: 4270px; overflow: hidden; background: var(--white); }
  body { position: relative; font-family: "Roboto", Arial, sans-serif; color: var(--ink); }
  .abs { position: absolute; }

  .masthead { left: 0; top: 0; width: 1200px; height: 174px; background: var(--blue); }
  .brand-name { left: 27px; top: 56px; font-family: "Varela Round", Arial, sans-serif; font-size: 56px; line-height: 1; color: var(--yellow); }
  .social { display: flex; gap: 26px; }
  .social span { width: 30px; height: 30px; border-radius: 50%; display: block; }
  .masthead .social { right: 30px; top: 72px; }
  .masthead .social span { background: var(--white); }

  .photo { background: linear-gradient(135deg, #cfd6d9, #9aa3a8 55%, #6d6358); }
  .hero { left: 30px; top: 202px; width: 1142px; height: 595px; }

  .section-title { left: 0; width: 1200px; text-align: center; font-weight: 300; color: var(--ink); letter-spacing: 2px; }
  .title-one { top: 895px; font-size: 47px; }
  .rule { left: 543px; top: 972px; width: 114px; height: 4px; background: var(--blue); }
  .mission { left: 90px; top: 1016px; width: 1020px; text-align: center; font-family: "Varela Round", Arial, sans-serif; font-size: 30px; line-height: 50px; color: var(--gold-text); font-weight: 700; }

  .service-photo { width: 548px; height: 358px; }
  .bar-left { border-left: 14px solid var(--yellow); }
  .bar-right { border-right: 14px solid var(--blue); }
  .service-title { font-weight: 300; font-size: 37px; line-height: 57px; letter-spacing: 1.5px; color: var(--ink); }
  .service-text { font-size: 23px; line-height: 45px; color: var(--ink); }
  .checklist { list-style: none; font-size: 23px; line-height: 45px; }
  .checklist li { display: flex; align-items: center; gap: 10px; }
  .checklist svg { flex: none; }

  .title-two { top: 2905px; font-size: 57px; }
  .meeting { left: 30px; top: 3021px; width: 1142px; height: 596px; background: linear-gradient(120deg, #b9ddc8, #7fb7a0 40%, #5c5048 75%, #d8d0c4); }

  .cta-join { left: 0; top: 3646px; width: 706px; height: 435px; background: var(--blue); }
  .cta-join h2 { position: absolute; left: 27px; top: 102px; font-family: "Varela Round", Arial, sans-serif; font-weight: 400; font-size: 43px; line-height: 60px; color: var(--white); letter-spacing: 1px; }
  .cta-button { position: absolute; left: 30px; top: 267px; width: 255px; height: 82px; border-radius: 6px; background: var(--yellow); color: var(--ink); font-size: 28px; font-weight: 500; display: flex; align-items: center; justify-content: center; text-decoration: none; }
  .cta-discover { left: 706px; top: 3646px; width: 494px; height: 435px; background: var(--yellow); display: flex; align-items: center; justify-content: center; }
  .cta-discover p { font-family: "Varela Round", Arial, sans-serif; font-size: 45px; line-height: 60px; color: var(--white); text-align: center; letter-spacing: 1px; }

  .legal { left: 0; top: 4122px; width: 1200px; text-align: center; font-size: 20px; line-height: 36px; color: var(--gray); }
  .footer-social { left: 525px; top: 4214px; gap: 30px; }
  .footer-social span { width: 28px; height: 28px; background: var(--blue); }
</style>
</head>
<body>

<header class="abs masthead">
  <div class="abs brand-name">Halvern Partners</div>
  <nav class="abs social" aria-label="Social links"><span></span><span></span><span></span></nav>
</header>

<div class="abs photo hero" role="img" aria-label="Consultant presenting to agency owners around a boardroom table"></div>

<h1 class="abs section-title title-one">M&amp;A TRANSACTIONS</h1>
<div class="abs rule"></div>
<p class="abs mission">Halvern Partners exists to help the owners of independent marketing communication agencies achieve their ambitions and maximize the value of their life's work.</p>

<div class="abs photo service-photo bar-left" style="left:35px;top:1235px;background:linear-gradient(160deg,#8d9296,#3c3f44 60%,#e0632a 70%,#2a2c30);" role="img" aria-label="Runner in a business suit crouched at a starting line marked 2020"></div>
<h2 class="abs service-title" style="left:650px;top:1273px;">SALES READINESS<br>ASSESSMENT</h2>
<p class="abs service-text" style="left:651px;top:1397px;width:500px;text-align:justify;">Make sure your agency is firing on all cylinders at the time of sale to maximize your current value and any potential earnout.</p>

<h2 class="abs service-title" style="left:50px;top:1673px;">FOUR-PHASE EXTERNAL<br>SALE PROCESS</h2>
<ul class="abs checklist" style="left:58px;top:1804px;">
  <li><svg width="20" height="20" viewBox="0 0 20 20"><circle cx="10" cy="10" r="8" fill="none" stroke="#0456a4" stroke-width="2.5"/><circle cx="10" cy="10" r="3.5" fill="#0456a4"/></svg>Readiness assessment</li>
  <li><svg width="20" height="20" viewBox="0 0 20 20"><circle cx="10" cy="10" r="8" fill="none" stroke="#0456a4" stroke-width="2.5"/><circle cx="10" cy="10" r="3.5" fill="#0456a4"/></svg>Valuation</li>
  <li><svg width="20" height="20" viewBox="0 0 20 20"><circle cx="10" cy="10" r="8" fill="none" stroke="#0456a4" stroke-width="2.5"/><circle cx="10" cy="10" r="3.5" fill="#0456a4"/></svg>Suitor identification</li>
  <li><svg width="20" height="20" viewBox="0 0 20 20"><circle cx="10" cy="10" r="8" fill="none" stroke="#0456a4" stroke-width="2.5"/><circle cx="10" cy="10" r="3.5" fill="#0456a4"/></svg>Transaction evaluation and negotiation</li>
</ul>
<div class="abs photo service-photo bar-right" style="left:620px;top:1634px;background:linear-gradient(135deg,#f4f4f4,#cfd3d6 50%,#3f7fc4);" role="img" aria-label="Compass dial pointing toward success"></div>

<div class="abs photo service-photo bar-left" style="left:35px;top:2034px;background:linear-gradient(120deg,#3b3a3a,#c9b7a0 45%,#f3efe6 70%,#2c3340);" role="img" aria-label="Two business people shaking hands"></div>
<h2 class="abs service-title" style="left:650px;top:2077px;">INTERNAL SALE</h2>
<p class="abs service-text" style="left:651px;top:2147px;width:460px;">Designed to transfer ownership to your designated successor over time, on your terms and where you stay in control throughout.</p>

<h2 class="abs service-title" style="left:50px;top:2557px;">EMPLOYEE STOCK<br>OWNERSHIP PLANS</h2>
<div class="abs photo service-photo bar-right" style="left:620px;top:2433px;background:linear-gradient(90deg,#5b84c0,#ffe600 12%,#ffe600 22%,#b9cde8 35%,#3e6db4);" role="img" aria-label="Employee stock ownership plan concept over financial figures"></div>

<h2 class="abs section-title title-two">M&amp;A TRANSACTIONS</h2>
<div class="abs meeting" role="img" aria-label="Two business partners in discussion at a table with a laptop"></div>

<section class="abs cta-join">
  <h2>Interested in Joining<br>halvernpartners</h2>
  <a class="cta-button" href="https://www.halvernpartners.example/">CONTACT US</a>
</section>
<section class="abs cta-discover">
  <p>Discover all<br>Services and<br>events for<br>your company</p>
</section>

<footer>
  <p class="abs legal">© 2020 Halvern Partners Consultancy, LLC. All Content is property of Halvern Partners Consultancy,<br>LLC. All Rights Reserved. Site by Tidewell Studio.</p>
  <nav class="abs social footer-social" aria-label="Social links"><span></span><span></span><span></span></nav>
</footer>

</body>
</html>
```